***Retail Packaging Card Design VERY SIMPLE FAST MONEY

Hey guys and gals...

I own a company that makes embroidered patches. We are getting ready to package our item for display in stores. To do so, we have these cool poly bags that seal at the bottom and then have a built-in hole at the top. All you need to do is insert the pre-printed cardstock card and the patch, and it is ready to hang on a wire retail rack.

We have two size bags, and the cards that fit in each will be:
4.25 inches wide x 5.5 inches tall
and
3.25 inches wide x 5.25 inches tall.

Once you have the patch inside, with the card, you are really only working with an available 1.5-inch section above that patch that shows. See examples below.

What I need: some designs for this card that will work with the various types of patches we make. I am willing to pick more than one winner and more than one design if more than one of these works out. I have five themes in mind, and if they are good enough, I am willing to buy all five separately.

First of all, the wording in the design is simply: IRON-ON PATCH.

From there, we want versions of this design that would look right on the following types of patches:

1) American Flag/Patriotic - this would be for a flag you might buy in a military surplus store or in a souvenir store in a city.

2) Rock and Roll - something that might work in a Marlowe's Novelties type of setting - imagine a biohazard patch or a skull and crossbones in the packaging.

3) Scuba Diving. We actually sell a ton of Scuba-related/Diver Down patches and need something specific to those types of stores.

4) Irish patches. Something with a Celtic and/or Ireland design would be great.

5) Generic International Flags. Instead of just one country flag, something that could easily be pictured housing the flag of any country. Some of our stores carry 50-60 styles here, so something that might work with all of them.

One of my main objectives with this product is that the logo/design be EASY TO READ. Imagine walking through a Marlowe's Novelties, a head shop, or an airport gift shop. These will be hanging on a wire rack, and that IRON-ON PATCH must be really easy to read. (That's why we're not doing Embroidered Patch for the text - the word Embroidered is just too hard to read from 5-8 feet and/or looks to squished in). Therefore, I would think the wording would take up a majority of the limited space.

The only other design tip I have is to avoid a white background. One of the sample I will upload has a white background, but a pattern or even just the plain black looks better with a patch inside.

Below I am attaching a few photo links - a couple of really generic mock-ups we did ourselves (they are serviceable but lack any real character, style, or look like they "fit" one of the categories above). I'm also attaching a photo of something similar that a competitor does, just so you can see a patch inside packaging an get a sense of what the final product might look like.

Some very generic mock-ups we've been working with:
http://brindlewoodgoods.example/misc/hangers3.jpg

What these look like with the patches in them:
http://brindlewoodgoods.example/misc/sample1.jpg
http://brindlewoodgoods.example/misc/sample2.jpg

A sample of a competitor's product inside bag with card similar to what you might design:

http://brindlewoodgoods.example/misc/USFLAG.jpg

If you have any questions, or if I have left anything out, please ask and I will post your answer here.

December 18 UPDATE TO DESIGNERS: We have some really good entries in for the "rock" and "patriotic" categories. If you want to submit on these, we encourage more designs, but bring your best. As for Irish, Scuba, and some sort of "works with any flag" category are still somewhat open (especially the first two). Would like to see something on the irish that incorporates either a clover (we sell one at keepsakestitch dot example that would be a good shape/style to use) or the Irish flag or Irish harp. As for the scuba, something red-themed possibly with the red Diver Down flag would be nice.

Requirements
Must have
• Easy to read
Should not have
• Anything too busy to affect readability. Especially any font that is too fancy. Size it to actual size on your screen, stand up and step back 5-8 feet. Is it a blur? Change it.

```html
<!DOCTYPE html>
<html lang="en">
<head>
<meta charset="utf-8">
<title>Iron-On Patch – Rock Hang Card</title>
<link rel="stylesheet" href="https://fonts.googleapis.com/css2?family=Righteous&display=swap">
<style>
  :root {
    --stage-red: #b5061f;
    --stage-red-deep: #7a0010;
    --card-navy: #1f3550;
    --card-navy-deep: #0d1826;
    --card-base: #0f1719;
    --fold-line: #2c3a40;
    --title-red: #e4202f;
    --title-edge: #fff4e6;
    --gold: #e0a93a;
    --art-dark: #2a1416;
    --art-red: #6b1c1c;
  }
  html, body {
    margin: 0;
    width: 1200px;
    height: 1000px;
    overflow: hidden;
  }
  body {
    background: radial-gradient(ellipse at 50% 20%, var(--stage-red) 0%, var(--stage-red-deep) 100%);
    font-family: "Righteous", "Arial Black", sans-serif;
  }
  .hang-card {
    position: absolute;
    left: 390px;
    top: 40px;
    width: 420px;
    height: 910px;
    filter: drop-shadow(0 10px 18px rgba(0, 0, 0, 0.45));
  }
  .hang-card svg { display: block; }
  .card-title {
    font-family: "Righteous", "Arial Black", sans-serif;
    fill: var(--title-red);
    stroke: var(--title-edge);
    stroke-width: 4;
    paint-order: stroke fill;
  }
</style>
</head>
<body>
  <div class="hang-card">
    <svg width="420" height="910" viewBox="0 0 420 910" xmlns="http://www.w3.org/2000/svg">
      <defs>
        <radialGradient id="panelGlow" cx="0.5" cy="0.78" r="0.85">
          <stop offset="0" stop-color="var(--card-navy-deep)"/>
          <stop offset="0.55" stop-color="var(--card-navy)"/>
          <stop offset="1" stop-color="#14253a"/>
        </radialGradient>
        <linearGradient id="cornerArt" x1="0" y1="0" x2="1" y2="1">
          <stop offset="0" stop-color="var(--art-red)"/>
          <stop offset="1" stop-color="var(--art-dark)"/>
        </linearGradient>
      </defs>

      <!-- main printed panel -->
      <rect class="card-panel" x="0" y="0" width="420" height="680" fill="url(#panelGlow)"/>

      <!-- corner artwork area -->
      <path class="corner-art" role="img" aria-label="Corner artwork: skull and electric guitar over red swirl"
            d="M135 0 H420 V135 Q300 40 135 0 Z" fill="url(#cornerArt)"/>
      <path class="corner-trim" d="M135 0 Q300 40 420 135" fill="none" stroke="var(--gold)" stroke-width="5"/>

      <!-- title -->
      <text class="card-title" x="14" y="112" font-size="70" textLength="380" lengthAdjust="spacingAndGlyphs">IRON-ON</text>
      <text class="card-title" x="14" y="188" font-size="70" textLength="380" lengthAdjust="spacing">PATCH</text>

      <!-- hanger tab with pennant point -->
      <path class="hanger-tab" d="M0 680 H420 V787 L210 908 L0 787 Z" fill="var(--card-base)"/>
      <line class="fold-line" x1="0" y1="681" x2="420" y2="681" stroke="var(--fold-line)" stroke-width="2" stroke-dasharray="5 4"/>
    </svg>
  </div>
</body>
</html>
```